Clearwater Renewal Pathway Institute Second Chance Recovery Services

Logo needs to incorporate that we are here to help support positive healthy lifestyle change and help with restoration of drivers license after getting caught driving under the influence of alcohol or other drugs. While enrolled in our 3-,6-, or 9-mo program we help clients explore their relationship with alcohol or other drugs and and seek help and support so that can overcome barriers that support a healthy life style supporting client decisions to change risky behavior like driving under the influence of alcohol or drugs.

Target Market(s)

DWI / DUI Clients

Contact Information for Business Card

Logo that signifies supportive services for positive change

Requirements
Must have
• Its more of a Alcohol and drug program / Interventions for self assessment / evaluation of relationship with alcohol or drug and or risky behavior s
Should not have
• Cars on indication of cars sales

```html
<!DOCTYPE html>
<html lang="en">
<head>
<meta charset="utf-8">
<title>Clearwater Renewal Pathway Institute – Business Card</title>
<link rel="stylesheet" href="https://fonts.googleapis.com/css2?family=Montserrat:wght@400;500;600;700&display=swap">
<style>
  :root {
    --page: #ffffff;
    --card-dark: #050505;
    --card-mid: #1a1a1a;
    --silver: #d9d9d9;
    --silver-bright: #f2f2f2;
    --silver-dim: #8a8a8a;
    --text: #ffffff;
  }
  * { box-sizing: border-box; margin: 0; padding: 0; }
  html, body {
    width: 734px; height: 1200px; overflow: hidden;
    background: var(--page);
    font-family: "Montserrat", sans-serif;
  }
  .sheet {
    width: 734px; height: 1200px;
    display: flex; flex-direction: column; align-items: center; justify-content: center;
    gap: 44px;
  }
  .card {
    position: relative;
    width: 620px; height: 354px;
    background:
      radial-gradient(ellipse at 55% 35%, var(--card-mid) 0%, var(--card-dark) 75%);
    box-shadow: 0 6px 14px rgba(0,0,0,.35);
    overflow: hidden;
    color: var(--text);
  }
  .card-lines { position: absolute; inset: 0; width: 100%; height: 100%; }

  /* front */
  .front-brand {
    position: absolute; left: 0; right: 0; top: 128px;
    text-align: center;
  }
  .brand-name {
    font-weight: 600; font-size: 44px; letter-spacing: 1px;
    color: var(--silver); line-height: 1;
  }
  .brand-tagline {
    margin-top: 8px;
    font-weight: 600; font-size: 7px; letter-spacing: .4px;
    color: var(--silver);
  }
  .front-url {
    position: absolute; left: 0; right: 0; top: 292px;
    text-align: center;
    font-weight: 500; font-size: 14px; letter-spacing: 1.6px;
  }

  /* back */
  .back-brand {
    position: absolute; left: 345px; width: 230px; top: 70px;
    text-align: center;
  }
  .back-brand .brand-name { font-size: 27px; }
  .back-brand .brand-tagline { font-size: 4.2px; margin-top: 6px; letter-spacing: .1px; }
  .holder { position: absolute; left: 40px; top: 137px; }
  .holder-name {
    font-weight: 700; font-size: 23px; letter-spacing: 1px; color: var(--silver-bright);
  }
  .holder-role { font-weight: 500; font-size: 11px; margin-top: 3px; }
  .contact-list { position: absolute; top: 226px; list-style: none; }
  .contact-list.left { left: 40px; }
  .contact-list.right { left: 331px; }
  .contact-item {
    display: flex; align-items: center; gap: 10px;
    font-weight: 500; font-size: 14px; letter-spacing: .5px;
    height: 20px; margin-bottom: 11px;
  }
  .contact-item svg { width: 13px; height: 13px; flex: none; fill: var(--silver-bright); }
</style>
</head>
<body>
<main class="sheet">

  <section class="card card-front" aria-label="Card front">
    <svg class="card-lines" viewBox="0 0 620 354" aria-hidden="true">
      <g stroke="var(--silver-dim)" stroke-width="1" fill="none">
        <polyline points="0,134 530,107 620,157"/>
      </g>
      <g stroke="var(--silver)" fill="none">
        <line x1="478" y1="0" x2="620" y2="100" stroke-width="2"/>
        <line x1="500" y1="0" x2="620" y2="84" stroke-width="1"/>
        <line x1="524" y1="0" x2="620" y2="68" stroke-width="3"/>
        <line x1="552" y1="0" x2="620" y2="48" stroke-width="1"/>
        <line x1="0" y1="245" x2="150" y2="354" stroke-width="2"/>
        <line x1="0" y1="270" x2="115" y2="354" stroke-width="1"/>
        <line x1="0" y1="293" x2="83" y2="354" stroke-width="3"/>
        <line x1="0" y1="318" x2="50" y2="354" stroke-width="1"/>
      </g>
    </svg>
    <div class="front-brand">
      <div class="brand-name">CLEARWATER</div>
      <div class="brand-tagline">CLEARWATER RENEWAL PATHWAY INSTITUTE SECOND CHANCE RECOVERY SERVICES</div>
    </div>
    <div class="front-url">WWW.CLEARWATERRENEWALPATHWAY.ORG</div>
  </section>

  <section class="card card-back" aria-label="Card back">
    <svg class="card-lines" viewBox="0 0 620 354" aria-hidden="true">
      <polyline points="0,200 277,200 318,169 620,169" stroke="var(--silver)" stroke-width="2" fill="none"/>
      <g stroke="var(--silver)" fill="none">
        <line x1="0" y1="262" x2="125" y2="354" stroke-width="2"/>
        <line x1="0" y1="285" x2="94" y2="354" stroke-width="1"/>
        <line x1="0" y1="307" x2="64" y2="354" stroke-width="3"/>
        <line x1="0" y1="330" x2="33" y2="354" stroke-width="1"/>
      </g>
    </svg>
    <div class="back-brand">
      <div class="brand-name">CLEARWATER</div>
      <div class="brand-tagline">CLEARWATER RENEWAL PATHWAY INSTITUTE SECOND CHANCE RECOVERY SERVICES</div>
    </div>
    <div class="holder">
      <div class="holder-name">DANIEL REYES</div>
      <div class="holder-role">Support restoration of drivers</div>
    </div>
    <ul class="contact-list left">
      <li class="contact-item">
        <svg viewBox="0 0 24 24"><path d="M6.6 10.8a15.1 15.1 0 0 0 6.6 6.6l2.2-2.2c.3-.3.7-.4 1-.2 1.1.4 2.3.6 3.6.6.6 0 1 .4 1 1V20c0 .6-.4 1-1 1A17 17 0 0 1 3 4c0-.6.4-1 1-1h3.5c.6 0 1 .4 1 1 0 1.3.2 2.5.6 3.6.1.3 0 .7-.2 1z"/></svg>
        555 014 2387
      </li>
      <li class="contact-item">
        <svg viewBox="0 0 24 24"><path d="M12 2a7 7 0 0 0-7 7c0 5.2 7 13 7 13s7-7.8 7-13a7 7 0 0 0-7-7zm0 9.5A2.5 2.5 0 1 1 12 6.5a2.5 2.5 0 0 1 0 5z"/></svg>
        your company location
      </li>
    </ul>
    <ul class="contact-list right">
      <li class="contact-item">
        <svg viewBox="0 0 24 24"><path d="M2 5h20v14H2zm2 2v.5l8 5 8-5V7l-8 5z"/></svg>
        hello@clearwaterrenewal.org
      </li>
      <li class="contact-item">
        <svg viewBox="0 0 24 24"><path d="M12 2a10 10 0 1 0 0 20 10 10 0 0 0 0-20zm6.9 6h-3a15 15 0 0 0-1.3-3.9A8 8 0 0 1 18.9 8zM12 4c.8 1.2 1.5 2.5 1.9 4h-3.8c.4-1.5 1.1-2.8 1.9-4zM4.3 14a8 8 0 0 1 0-4h3.4a16 16 0 0 0 0 4zm.8 2h3a15 15 0 0 0 1.3 3.9A8 8 0 0 1 5.1 16zm3-8h-3a8 8 0 0 1 4.3-3.9C8.8 5.3 8.4 6.6 8.1 8zM12 20c-.8-1.2-1.5-2.5-1.9-4h3.8c-.4 1.5-1.1 2.8-1.9 4zm2.3-6H9.7a14 14 0 0 1 0-4h4.6a14 14 0 0 1 0 4zm.3 5.9c.6-1.2 1-2.5 1.3-3.9h3a8 8 0 0 1-4.3 3.9zM16.3 14a16 16 0 0 0 0-4h3.4a8 8 0 0 1 0 4z"/></svg>
        www.clearwaterrenewal.org
      </li>
    </ul>
  </section>

</main>
</body>
</html>
```